Bref créative
Logo for coaching business
Bus card design, stationary/letterhead, envelopes
Professional
Gerald Pinsky
International Author - Coach - Mentor
20583 W. Marigold Ave. #215-347
Scottsdale, AZ 85917
Gerald@brightkestrelcoaching.example
www.BrightKestrelCoaching.example
Need additional bus. card layout for-
Tom Ridgely, MMAC
Life Coach - Counselor
Tom@brightkestrelcoaching.example

```html
<!DOCTYPE html>
<html lang="en">
<head>
<meta charset="utf-8">
<title>Bright Kestrel Coaching – Business Card</title>
<link href="https://fonts.googleapis.com/css2?family=Marcellus+SC&display=swap" rel="stylesheet">
<style>
  :root {
    --page-bg: #e9e6e1;
    --card-bg: #ffffff;
    --brand-blue: #1f6fb2;
    --brand-green: #3aa43a;
    --brand-purple: #8e2a8a;
    --text-grey: #5a5a5a;
    --icon-grey: #6b6b6b;
    --rule-grey: #c9c9c9;
  }
  html, body {
    margin: 0;
    width: 1200px;
    height: 914px;
    overflow: hidden;
    background: var(--page-bg);
  }
  .card {
    position: absolute;
    left: 100px;
    top: 167px;
    width: 1000px;
    height: 580px;
    background: var(--card-bg);
    box-shadow: 0 12px 30px rgba(0,0,0,0.18);
    font-family: "Marcellus SC", serif;
    color: var(--text-grey);
    overflow: hidden;
  }
  .brand {
    position: absolute;
    left: 300px;
    top: 110px;
    display: flex;
    align-items: center;
    gap: 18px;
  }
  .brand-mark {
    width: 70px;
    height: 70px;
    border-radius: 50%;
    background: var(--brand-blue);
  }
  .brand-name {
    font-size: 44px;
    color: var(--brand-blue);
    letter-spacing: 1px;
    line-height: 1;
  }
  .tagline {
    position: absolute;
    left: 390px;
    top: 176px;
    font-size: 16px;
    letter-spacing: 1px;
    white-space: nowrap;
  }
  .tagline .t-green { color: var(--brand-green); }
  .tagline .t-purple { color: var(--brand-purple); }
  .tagline .t-blue { color: var(--brand-blue); }
  .person {
    position: absolute;
    right: 520px;
    top: 240px;
    text-align: right;
    font-size: 19px;
    line-height: 28px;
    white-space: nowrap;
  }
  .person-name {
    color: var(--brand-blue);
    font-size: 24px;
    line-height: 32px;
  }
  .divider {
    position: absolute;
    left: 498px;
    top: 272px;
    width: 1px;
    height: 112px;
    background: var(--rule-grey);
  }
  .contacts {
    position: absolute;
    left: 512px;
    top: 272px;
    list-style: none;
    margin: 0;
    padding: 0;
    font-size: 18px;
    line-height: 28px;
    white-space: nowrap;
  }
  .contacts li {
    display: flex;
    align-items: center;
    gap: 10px;
  }
  .contacts svg { width: 18px; height: 18px; flex: none; }
  .bands {
    position: absolute;
    left: 0;
    bottom: 0;
    width: 1000px;
    height: 130px;
  }
</style>
</head>
<body>
  <div class="card">
    <div class="brand">
      <span class="brand-mark"></span>
      <span class="brand-name">Bright Kestrel Coaching</span>
    </div>
    <div class="tagline">
      <span class="t-green">Clear Focus</span> ·
      <span class="t-purple">Steady Growth</span> ·
      <span class="t-blue">Fresh Start</span>
    </div>

    <div class="person">
      <div class="person-name">Gerald Pinsky</div>
      <div class="person-role">International Author · Coach · Mentor</div>
      <div class="person-address">20583 W. Marigold Ave. #215-347</div>
      <div class="person-city">Scottsdale, AZ 85917</div>
    </div>

    <div class="divider"></div>

    <ul class="contacts">
      <li>
        <svg viewBox="0 0 20 20" aria-hidden="true"><circle cx="10" cy="10" r="10" fill="var(--icon-grey)"/><path d="M7 5.5l1.6 2.3-1 1.1c.6 1.3 1.6 2.3 2.9 2.9l1.1-1 2.3 1.6-.8 1.8c-3.8-.4-6.6-3.2-7-7z" fill="#fff"/></svg>
        <span>555-555-0142</span>
      </li>
      <li>
        <svg viewBox="0 0 20 20" aria-hidden="true"><circle cx="10" cy="10" r="10" fill="var(--icon-grey)"/><rect x="5" y="6.5" width="10" height="7" fill="#fff"/><path d="M5 6.5l5 4 5-4" fill="none" stroke="var(--icon-grey)" stroke-width="1"/></svg>
        <span>Gerald@brightkestrelcoaching.example</span>
      </li>
      <li>
        <svg viewBox="0 0 20 20" aria-hidden="true"><circle cx="10" cy="10" r="10" fill="var(--icon-grey)"/><circle cx="10" cy="10" r="5" fill="none" stroke="#fff" stroke-width="1.2"/><path d="M5 10h10M10 5c-2.5 3-2.5 7 0 10M10 5c2.5 3 2.5 7 0 10" fill="none" stroke="#fff" stroke-width="1"/></svg>
        <span>www.BrightKestrelCoaching.example</span>
      </li>
    </ul>

    <svg class="bands" viewBox="0 0 1000 130" preserveAspectRatio="none" aria-hidden="true">
      <defs>
        <linearGradient id="blueBand" x1="0" y1="0" x2="0" y2="1">
          <stop offset="0" stop-color="#2f86cc"/>
          <stop offset="1" stop-color="#1a5f9e"/>
        </linearGradient>
        <linearGradient id="greenBand" x1="0" y1="0" x2="0" y2="1">
          <stop offset="0" stop-color="#4cbb3f"/>
          <stop offset="1" stop-color="#2e8f2e"/>
        </linearGradient>
      </defs>
      <polygon points="0,20 600,20 640,62 0,62" fill="url(#blueBand)"/>
      <polygon points="560,62 1000,62 1000,110 610,110" fill="url(#greenBand)"/>
    </svg>
  </div>
</body>
</html>
```